Quiet Harbor, LLC Business Card Design

We need a product business card designed for a new company Quiet Harbor, LLC. We make and resell waterless RV cleaner, polish and protectant. It cleans and protects in a simple spray and wipe step leaving the surface protected and conditioned to repel dust, dirt, water, smudges, bugs and fingerprints while preventing fogging. Safe on acrylic, plexiglas, lexan, plastic, rubber, painted surfaces, chrome, stainless, aluminum, vinyl, leather, glass.... This is an eco-friendly green product.

We want to play off the company name to tell the consumer that the product is easy to use and associate to the nostalgics 1950's in the USA... Thinking old travel trailer with hot rod truck pulling it as the graphic, maybe the husband cleaning the truck and the wife cleaning the trailer for a Quiet Harbor surface.
Updates

Just posted our newly finished logo. Need to have "Cleaner and Protectant" added to the design as well. Thanks everyone that has submitted thus far, i am working to get comments on all.

If you need a different file format, please let me know. Thank you.

Most important info, is the logo, website and the words "Cleaner" or "Clean" along "Protectant" or "Protect" the remainder is of less importance. Highlight: www.quietharborwash.example Focus is on company brand for Quieter Harbor Cleaner product: However, need a section for the following contact info: Walt Brinkley (xxx) xxx-xxxx email address Would like space for QR Code if possible.

Target Market(s)

Adults in the USA between ages of 35-75 that are actively involved in the Recreational Vehicle (RV), travel trailer, and hot rod lifestyle. We are targeting the RV marked of the high end travel, 5th wheel and bus RV market. Along with hot rods, automotive and motorcycle market.

Industry/Entity Type

Travel

Requirements
Must have
• Most important info, is the logo, website and the words "Cleaner" or "Clean" along "Protectant" or "Protect" the remainder is of less importance.

Highlight:
www.quietharborwash.example

Focus is on company brand for Quieter Harbor Cleaner product: However, need a section for the following contact info:

Walt Brinkley
(xxx) xxx-xxxx
email address
Nice to have
• Would like a space for a QR Code.

```html
<!DOCTYPE html>
<html lang="en">
<head>
<meta charset="utf-8">
<title>Quiet Harbor, LLC – Business Card</title>
<link href="https://fonts.googleapis.com/css2?family=Open+Sans:wght@400;600;700&family=Playball&display=swap" rel="stylesheet">
<style>
  :root {
    --backdrop: #1f1e1f;
    --card-white: #ffffff;
    --card-dark: #2b292a;
    --card-dark-deep: #1c1b1c;
    --brand-blue: #1a6fc2;
    --ink: #1a1a1a;
    --strip: #ececec;
    --strip-text: #2a2a2a;
  }
  * { box-sizing: border-box; margin: 0; padding: 0; }
  html, body {
    width: 1200px; height: 800px; overflow: hidden;
    background: var(--backdrop);
    font-family: "Open Sans", Arial, sans-serif;
  }
  .canvas { position: relative; width: 1200px; height: 800px; }
  .card {
    position: absolute; left: 320px;
    width: 560px; height: 320px;
    overflow: hidden;
    box-shadow: 0 12px 30px rgba(0,0,0,.55);
  }
  /* Front */
  .card-front { top: 50px; background: var(--card-white); }
  .card-front .edge-swoosh { position: absolute; inset: 0; width: 100%; height: 100%; }
  .brand-name {
    font-family: "Playball", cursive;
    font-weight: 400;
    white-space: nowrap;
  }
  .card-front .brand-name {
    position: absolute; left: 0; right: 0; top: 124px;
    text-align: center; font-size: 50px; line-height: 1.2; color: var(--ink);
  }
  /* Back */
  .card-back {
    top: 420px;
    background: linear-gradient(160deg, var(--card-dark) 0%, #3a3839 45%, var(--card-dark-deep) 100%);
  }
  .band { position: absolute; left: 0; right: 0; background: var(--card-white); }
  .band-top { top: 14px; height: 8px; }
  .band-bottom { bottom: 14px; height: 10px; }
  .card-back .brand-name {
    position: absolute; right: 26px; top: 98px;
    font-size: 36px; line-height: 1.2; color: var(--brand-blue);
  }
  .holder { position: absolute; left: 200px; top: 60px; }
  .holder-name { font-size: 16px; font-weight: 700; color: var(--card-white); line-height: 1.2; }
  .holder-role { font-size: 11px; color: var(--brand-blue); line-height: 1.3; }
  .contact-list { position: absolute; left: 22px; top: 150px; list-style: none; }
  .contact-item {
    display: flex; align-items: center; gap: 10px;
    height: 26px; margin-bottom: 10px; padding: 0 12px;
    background: var(--strip); color: var(--strip-text);
    font-size: 12px; width: max-content;
  }
  .contact-item svg { width: 12px; height: 12px; fill: var(--brand-blue); flex: none; }
</style>
</head>
<body>
<main class="canvas">

  <section class="card card-front" aria-label="Card front">
    <svg class="edge-swoosh" viewBox="0 0 560 320" preserveAspectRatio="none" aria-hidden="true">
      <path d="M0 0 Q 8 240 42 320 L 0 320 Z" fill="var(--brand-blue)"/>
      <path d="M560 320 Q 552 80 518 0 L 560 0 Z" fill="var(--brand-blue)"/>
    </svg>
    <p class="brand-name">Quiet Harbor, LLC</p>
  </section>

  <section class="card card-back" aria-label="Card back">
    <div class="band band-top"></div>
    <div class="holder">
      <p class="holder-name">Walt Brinkley</p>
      <p class="holder-role">Cleaner &amp; Protectant</p>
    </div>
    <p class="brand-name">Quiet Harbor, LLC</p>
    <ul class="contact-list">
      <li class="contact-item">
        <svg viewBox="0 0 24 24" aria-hidden="true"><path d="M6.6 10.8a15 15 0 0 0 6.6 6.6l2.2-2.2a1 1 0 0 1 1-.25 11.4 11.4 0 0 0 3.6.6 1 1 0 0 1 1 1V20a1 1 0 0 1-1 1A17 17 0 0 1 3 4a1 1 0 0 1 1-1h3.5a1 1 0 0 1 1 1c0 1.25.2 2.45.6 3.6a1 1 0 0 1-.25 1z"/></svg>
        555-014-2260
      </li>
      <li class="contact-item">
        <svg viewBox="0 0 24 24" aria-hidden="true"><path d="M6.6 10.8a15 15 0 0 0 6.6 6.6l2.2-2.2a1 1 0 0 1 1-.25 11.4 11.4 0 0 0 3.6.6 1 1 0 0 1 1 1V20a1 1 0 0 1-1 1A17 17 0 0 1 3 4a1 1 0 0 1 1-1h3.5a1 1 0 0 1 1 1c0 1.25.2 2.45.6 3.6a1 1 0 0 1-.25 1z"/></svg>
        555-014-2261
      </li>
      <li class="contact-item">
        <svg viewBox="0 0 24 24" aria-hidden="true"><path d="M2 5h20v14H2z M2 5l10 8 10-8"/></svg>
        walt@quietharborwash.example
      </li>
      <li class="contact-item">
        <svg viewBox="0 0 24 24" aria-hidden="true"><path d="M12 2a7 7 0 0 0-7 7c0 5 7 13 7 13s7-8 7-13a7 7 0 0 0-7-7zm0 9.5A2.5 2.5 0 1 1 12 6.5a2.5 2.5 0 0 1 0 5z"/></svg>
        www.quietharborwash.example
      </li>
    </ul>
    <div class="band band-bottom"></div>
  </section>

</main>
</body>
</html>
```